Superfoods Nutrition for Elderly

We need a thematic packaging design that fits our elderly nutrition products, that is based on our "3 Ws ethos" - eating Wisely, Widely & Wholly.

Wisely - selected superfoods and ingredients - NZ and other sources
Widely - based on the "rainbow diet" philosophy
Wholly - all natural, (no artificial flavours, colors etc). Formulated as complete meals (NOT supplementation)

Mediums:
- 400-450gram re-sealable doy packs
- 400-450gram re-sealable tin cans

Look n Feel:
Korunui - https://korunuipantry.com
Mela Vo - https://www.melvo.example.nz/
Lantern ridge - https://dinebrightstaybright.example.nz/collections/cereals

The name of our products may/may not be “tuatara bowl”. Our on-going research tells us that for the Asian market, an icon or character to personify our product may be a sound strategy. This is only for the designer to take note off.

Deliverables:
* 5 packaging designs in the range.
1x yellow + orange colored foods (star ingredient: “sun kept” – passion fruit powder)
1x red colored foods (star ingredient: (star ingredient: - Manuka honey )
1x blues/purple colored foods: (star ingredient: nolari blackcurrant)
1 x green coloured foods (star ingredient: Green kiwi)
1 x brown/white (star ingredients: brandon’s grass fed bone broth)

brand name, please use “TuataraBowl” for now.

These will be the products:

Blue/purple: “Instant oatmeal porridge”
Ingredients: Rolled Baby Oats, Blueberries, Blackcurrant Powder, chia seeds, Blue Spirulina, Sheep’s Milk.
Star ingredient: Blackcurrant powder (support eyesight)

Brown/White: “Instant Brown Rice”
Ingredients: Organic Brown Rice, Grass fed bone broth powder, collagen peptide powder, black sesame seeds, onions and garlic powder, dried mushrooms, probiotics.
Star ingredient: Grass fed bone broth (support joint health)

Green: “Instant Smoothie”
Ingredients: Organic Green Kiwifruit, Kale powder, green apple powder, whey protein concentrate, probiotics, and sheep’s milk powder
Star ingredient: Organic green kiwi fruit(supports immunity)

Yellow/Orange “Instant Oatmeal”
Ingredients: Organic rolled baby oats, banana, organic passionfruit, apricot, dried mango, probiotics, cinnamon, sheep’s milk powder.
Star ingredient: Organic passionfruit(regulates blood glucose)

Red: “ instant amaranth cereal”
Ingredients: Organic amaranth, red apples, pomegranate, cranberries, Manuka honey powder, probiotics, sheep’s milk
Star ingredient: Manuka honey powder (anti-inflammatory)

Target Market(s)

Whose attention we are trying to grab?

Primary:
- 20 to 40 year olds buying these products for their parents/grand parents
- Health Nutrition conscious “golden agers”
Secondary
- Professional Caregivers to the elderly (homes, private hospitals etc)
- 40 year olds in the “prevention” mind set.

Font styles to use
Serif
Sans Serif

Colors

Designer to choose colors to be used in the design.

Requirements
Must have
• Mandatory:
• - clear visual que of the food color/s
• - "New Zealand" origin must come through strongly.
• - must have a blurp or feature of the star ingredient for each with mention of brand.
• e.g. for the blues+ purple, NZ blackcurrant powder for improved eyesight (cataract prevention).
• - icons for “heart health, “eyesight”, “mobility”, “gut-health”.
• - every other ingredient must be stated.
• The name of product may/may not be “tuatarabowl”. Our on-going research tells us that for the Asian market, an icon or character to personify our product may be a sound strategy. This is only for the designer to take note off.
Nice to have
• Desirables:
• Ingredient origin story - e.g blackcurrant comes from Timaru etc.
• (refer to Pembertons destination marketing…)

```html
<!DOCTYPE html>
<html lang="en">
<head>
<meta charset="utf-8">
<title>TuataraBowl Instant Oatmeal Porridge – Pouch Front</title>
<link rel="stylesheet" href="https://fonts.googleapis.com/css2?family=Quicksand:wght@500;600;700&display=swap">
<style>
  :root {
    --page-bg: #f4f4f4;
    --pouch-white: #ffffff;
    --pouch-edge: #e6e6e6;
    --ink-dark: #1e1e1e;
    --purple-deep: #4f2488;
    --purple-light: #a27ccb;
    --purple-pill: #5b2b8f;
    --rule: #9a7cc0;
    --icon-grey: #8a8a8a;
    --label-grey: #9a9a9a;
    --porridge: #d8cabb;
    --berry: #2a2233;
  }
  * { box-sizing: border-box; margin: 0; padding: 0; }
  html, body { width: 1200px; height: 1200px; overflow: hidden; }
  body {
    background: var(--page-bg);
    font-family: "Quicksand", sans-serif;
    position: relative;
  }
  .pouch {
    position: absolute;
    left: 280px; top: 40px;
    width: 640px; height: 1120px;
    background: var(--pouch-white);
    border: 1px solid var(--pouch-edge);
    border-radius: 14px;
  }
  .zip-line {
    position: absolute; left: 0; right: 0; height: 2px;
    background: var(--pouch-edge);
  }
  .zip-line.first { top: 110px; }
  .zip-line.second { top: 142px; }
  .abs { position: absolute; left: 0; right: 0; text-align: center; }
  .brand-name {
    top: 300px;
    font-size: 62px; font-weight: 700;
    color: var(--ink-dark);
    letter-spacing: -1px;
  }
  .rule {
    position: absolute; left: 138px; width: 364px; height: 1px;
    background: var(--rule);
  }
  .rule.upper { top: 389px; }
  .rule.lower { top: 516px; }
  .product-title {
    top: 392px;
    font-size: 60px; font-weight: 700; line-height: 60px;
    background: linear-gradient(90deg, var(--purple-deep), var(--purple-light));
    -webkit-background-clip: text; background-clip: text;
    color: transparent;
  }
  .made-with {
    top: 525px; font-size: 18px; font-weight: 600; color: var(--purple-deep);
  }
  .star-ingredient {
    top: 546px; font-size: 30px; font-weight: 700; color: var(--purple-deep);
  }
  .benefit-pill {
    position: absolute; top: 588px; left: 50%; transform: translateX(-50%);
    background: var(--purple-pill); color: #fff;
    font-size: 18px; font-weight: 600;
    padding: 1px 9px; border-radius: 10px; white-space: nowrap;
  }
  .serving-photo {
    position: absolute; left: 85px; top: 650px;
    width: 470px; height: 300px;
    background:
      radial-gradient(circle at 50% 50%, var(--porridge) 0 128px, #ffffff 129px 136px, transparent 138px),
      radial-gradient(ellipse 70px 95px at 15% 48%, var(--berry) 0 80%, transparent 100%),
      radial-gradient(ellipse 55px 80px at 86% 58%, var(--berry) 0 80%, transparent 100%);
  }
  .benefit-rule {
    position: absolute; left: 120px; width: 400px; height: 1px;
    background: var(--rule);
  }
  .benefit-rule.top { top: 950px; }
  .benefit-rule.bottom { top: 1035px; }
  .benefits {
    position: absolute; top: 960px; left: 120px; width: 400px;
    display: flex; justify-content: space-between;
  }
  .benefit {
    width: 96px; text-align: center;
    font-size: 13px; color: var(--label-grey); font-weight: 500;
  }
  .benefit svg { display: block; margin: 0 auto 6px; height: 48px; }
  .net-weight {
    top: 1055px; font-size: 20px; font-weight: 500; color: var(--purple-deep);
  }
</style>
</head>
<body>
  <div class="pouch">
    <div class="zip-line first"></div>
    <div class="zip-line second"></div>

    <div class="abs brand-name">TuataraBowl</div>
    <div class="rule upper"></div>
    <h1 class="abs product-title">Instant Oatmeal<br>Porridge</h1>
    <div class="rule lower"></div>

    <div class="abs made-with">Made With</div>
    <div class="abs star-ingredient">Nolari Blackcurrant</div>
    <div class="benefit-pill">Supports Eyesight</div>

    <div class="serving-photo" role="img" aria-label="Bowl of blackcurrant oatmeal porridge with fresh blackcurrants on either side"></div>

    <div class="benefit-rule top"></div>
    <div class="benefits">
      <div class="benefit">
        <svg viewBox="0 0 48 48" width="48"><path d="M24 42 C8 30 4 22 4 15 C4 9 9 5 14 5 C19 5 22 8 24 11 C26 8 29 5 34 5 C39 5 44 9 44 15 C44 22 40 30 24 42Z" fill="var(--icon-grey)"/></svg>
        Heart Health
      </div>
      <div class="benefit">
        <svg viewBox="0 0 80 48" width="80"><path d="M2 24 C18 6 62 6 78 24 C62 42 18 42 2 24Z" fill="none" stroke="var(--icon-grey)" stroke-width="4"/><circle cx="40" cy="24" r="11" fill="none" stroke="var(--icon-grey)" stroke-width="5"/><circle cx="40" cy="24" r="4" fill="var(--icon-grey)"/></svg>
        Eyesight
      </div>
      <div class="benefit">
        <svg viewBox="0 0 48 48" width="48"><circle cx="32" cy="7" r="4" fill="var(--icon-grey)"/><path d="M18 16 L28 14 L26 26 L34 32 L32 42 M26 26 L18 32 L10 32 M28 14 L36 22 L42 20 M22 16 L14 22" fill="none" stroke="var(--icon-grey)" stroke-width="4" stroke-linecap="round" stroke-linejoin="round"/></svg>
        Mobility
      </div>
      <div class="benefit">
        <svg viewBox="0 0 48 48" width="48"><path d="M20 3 V12 C20 16 24 16 28 16 C36 16 40 22 38 30 C36 38 28 40 22 38 C18 37 16 40 16 44 M20 12 C14 12 12 18 16 22" fill="none" stroke="var(--icon-grey)" stroke-width="2.5" stroke-linecap="round"/></svg>
        Gut-Health
      </div>
    </div>
    <div class="benefit-rule bottom"></div>

    <div class="abs net-weight">Net weight: 450g</div>
  </div>
</body>
</html>
```